Need Plexora Ads for Tyre Company

Need some plexora ads graphics for our tyre company Tyre Ferns that only operates in the cayman islands.

Need Ratio Ads: 1000x1000, 1910x1000, 300x600

Important things to have the customer know:
-Email : info@tyreferns.example
-Phone: +1 345 555 0142
-Address: 41 Marlow Lane, George Town, Cayman Islands
-Website: tyreferns.example (Please see our website for the tyres we offer)
- Common Car brands that our Tyres are compatible with: Kelvar, Pratova, Zolt Quira, Bexmont, Tavel, Lorimo, Feravi, Drastelmor
- Our tyres are priced from KYD$55-$60
-We offer free installation on tyres when customers come to our facility to get them changed.
-We sell tyres in bulk and individually.

*You can choose which things to add or omit for the best look, feel free to reword any of the above also to better fit in.
*Please keep in mind that these will have to be viewed in small formats aswell since they are for plexora ads. Please ensure everything is readable when zoomed out.

Target Market(s)

car rental companies & individuals who need to get their tyres replace

Industry/Entity Type

Automotive, Tyre replacement, Car Parts

Colors
EB3D1F
EC4F4E
F09395
F8D3D4
FCEDEE

Requirements
Must have
• Phone, Location, Brands that our tyres are compatible with, Same theme as our logo(Red & Black, White), design adapted to the 3 ratios listed above
Nice to have
• Creative advertising

```html
<!DOCTYPE html>
<html lang="en">
<head>
<meta charset="utf-8">
<title>Tyre Ferns – Ad Set</title>
<link href="https://fonts.googleapis.com/css2?family=Exo+2:ital,wght@1,700;1,800&family=Jost:wght@400;500;600;700&family=Inter:wght@400;500;600&display=swap" rel="stylesheet">
<style>
  :root{
    --red:#eb3d1f;
    --ink:#111111;
    --white:#ffffff;
    --muted:#d8d2d0;
    --page:#ffffff;
    --photo-dark:#141011;
    --photo-mid:#3c3030;
    --photo-warm:#6a3a2c;
    --photo-steel:#6e6869;
    --frame:#1b1b1b;
  }
  *{margin:0;padding:0;box-sizing:border-box}
  html,body{width:800px;height:1200px;overflow:hidden;background:var(--page)}
  body{position:relative;font-family:"Inter",sans-serif;color:var(--ink)}

  .size-label{position:absolute;font-family:"Inter",sans-serif;font-size:20px;font-weight:400;line-height:1;color:var(--ink)}

  .ad{position:absolute;overflow:hidden;background:var(--white);border:1px solid var(--frame)}
  .ad-photo{position:absolute;left:0;top:0;width:100%;
    background:
      radial-gradient(ellipse 28% 42% at 76% 62%,rgba(110,104,105,.55) 0%,rgba(60,48,48,.35) 45%,rgba(0,0,0,0) 75%),
      radial-gradient(ellipse 30% 55% at 20% 70%,rgba(106,58,44,.55) 0%,rgba(60,36,30,.3) 50%,rgba(0,0,0,0) 80%),
      radial-gradient(ellipse 40% 30% at 85% 10%,rgba(90,84,86,.35) 0%,rgba(0,0,0,0) 70%),
      linear-gradient(160deg,#2a2021 0%,var(--photo-dark) 55%,#0c0a0b 100%)}

  .headline{position:absolute;font-family:"Exo 2",sans-serif;font-style:italic;font-weight:800;color:var(--white);line-height:1;white-space:nowrap}
  .headline .accent{color:var(--red)}
  .rule{position:absolute;height:2px;background:var(--white)}
  .tagline{position:absolute;font-family:"Inter",sans-serif;color:var(--white);line-height:1.15}
  .price-label{position:absolute;font-family:"Inter",sans-serif;font-weight:500;letter-spacing:.08em;color:var(--white);text-transform:uppercase;white-space:nowrap}
  .price{position:absolute;font-family:"Jost",sans-serif;font-weight:700;color:var(--white);line-height:1;white-space:nowrap}
  .cta{position:absolute;background:var(--red);color:var(--white);font-family:"Exo 2",sans-serif;font-style:italic;font-weight:800;letter-spacing:.06em;text-transform:uppercase;display:flex;align-items:center;justify-content:center}
  .brand{position:absolute;display:flex;align-items:center;font-family:"Jost",sans-serif;font-weight:700;color:var(--white);white-space:nowrap;line-height:1}
  .brand-dot{border-radius:50%;border:2px solid var(--white);flex:none}
  .fits{position:absolute;font-family:"Inter",sans-serif;font-weight:500;color:var(--muted);line-height:1.3}
  .fits b{color:var(--white);font-weight:600;text-transform:uppercase;letter-spacing:.06em}

  .contact{font-family:"Jost",sans-serif;color:var(--ink);white-space:nowrap}
  .contact b{color:var(--red);font-weight:500}
  .contact-line{position:absolute;text-align:center}
  .contact-stack{position:absolute;display:flex;flex-direction:column;line-height:1.2}

  .center{left:0;right:0;text-align:center}

  .divider-shadow{position:absolute;left:117px;top:442px;width:561px;height:14px;
    background:radial-gradient(ellipse at 50% 0%,rgba(0,0,0,.85) 0%,rgba(0,0,0,.35) 35%,rgba(0,0,0,0) 70%)}
</style>
</head>
<body>

<!-- 1910 x 1000 -->
<div class="size-label" style="left:17px;top:26px">1910 x 1000</div>
<div class="ad" style="left:18px;top:55px;width:764px;height:321px;border:none">
  <div class="ad-photo" style="height:321px" role="img" aria-label="Photo: mechanic fitting a wheel on a dark car in a workshop"></div>
  <div class="headline center" style="top:84px;font-size:32px"><span class="accent">Free</span> Tyre Installation</div>
  <div class="rule" style="left:342px;top:132px;width:80px"></div>
  <div class="tagline center" style="top:148px;font-size:14px">We sell tyres in bulk and individually.</div>
  <div class="price-label center" style="top:178px;font-size:8.5px">Our tyres are priced from</div>
  <div class="price center" style="top:192px;font-size:33px">KYD$55-$60</div>
  <div class="cta" style="left:328px;top:242px;width:108px;height:24px;font-size:11px">Order now</div>
  <div class="fits center" style="top:282px;font-size:9px"><b>Compatible with</b> Kelvar · Pratova · Zolt · Quira · Bexmont · Tavel · Lorimo · Feravi · Drastelmor</div>
</div>
<div class="contact contact-line" style="left:0;right:0;top:393px;font-size:14px">
  <b>E.</b> info@tyreferns.example | <b>P.</b> +1 345 555 0142 | <b>W.</b> tyreferns.example
</div>
<div class="contact contact-line" style="left:0;right:0;top:415px;font-size:12px">
  <b>A.</b> 41 Marlow Lane, George Town, Cayman Islands
</div>
<div class="divider-shadow"></div>

<!-- 1000 x 1000 -->
<div class="size-label" style="left:17px;top:493px">1000 x 1000</div>
<div class="ad" style="left:18px;top:524px;width:400px;height:400px">
  <div class="ad-photo" style="height:344px" role="img" aria-label="Photo: mechanic fitting a wheel on a dark car in a workshop"></div>
  <div class="brand" style="left:27px;top:46px;font-size:27px;gap:7px"><span class="brand-dot" style="width:22px;height:22px"></span>Tyre Ferns</div>
  <div class="headline" style="left:27px;top:130px;font-size:30px"><span class="accent">Free</span> Tyre</div>
  <div class="headline" style="left:27px;top:162px;font-size:30px">Installation</div>
  <div class="rule" style="left:27px;top:202px;width:80px"></div>
  <div class="tagline" style="left:27px;top:216px;font-size:14px">We sell tyres in bulk and individually.</div>
  <div class="price-label" style="left:27px;top:244px;font-size:9px">Our tyres are priced from</div>
  <div class="price" style="left:27px;top:258px;font-size:32px">KYD$55-$60</div>
  <div class="fits" style="left:27px;top:302px;width:350px;font-size:9px"><b>Compatible with</b> Kelvar · Pratova · Zolt · Quira · Bexmont · Tavel · Lorimo · Feravi · Drastelmor</div>
  <div class="contact contact-line" style="left:0;right:0;top:353px;font-size:13px">
    <b>E.</b> info@tyreferns.example | <b>P.</b> +1 345 555 0142
  </div>
  <div class="contact contact-line" style="left:0;right:0;top:373px;font-size:13px">
    <b>W.</b> tyreferns.example | <b>A.</b> 41 Marlow Lane, George Town
  </div>
</div>

<!-- 300 x 600 -->
<div class="size-label" style="left:452px;top:493px">300 x 600</div>
<div class="ad" style="left:452px;top:524px;width:121px;height:241px">
  <div class="ad-photo" style="height:188px" role="img" aria-label="Photo: car wheel and mechanic in a workshop"></div>
  <div class="brand" style="left:10px;top:14px;font-size:12px;gap:4px"><span class="brand-dot" style="width:10px;height:10px;border-width:1.5px"></span>Tyre Ferns</div>
  <div class="headline" style="left:10px;top:52px;font-size:14px"><span class="accent">Free</span> Tyre</div>
  <div class="headline" style="left:10px;top:66px;font-size:14px">Installation</div>
  <div class="rule" style="left:10px;top:84px;width:33px;height:1px"></div>
  <div class="tagline" style="left:10px;top:91px;width:100px;font-size:7px">We sell tyres in bulk and individually.</div>
  <div class="price-label" style="left:10px;top:113px;font-size:5.6px">Our tyres are priced from</div>
  <div class="price" style="left:10px;top:122px;font-size:14px">KYD$55-$60</div>
  <div class="cta" style="left:10px;top:142px;width:66px;height:14px;font-size:7px">Order now</div>
  <div class="fits" style="left:10px;top:161px;width:104px;font-size:5.2px"><b>Fits</b> Kelvar · Pratova · Zolt · Quira · Bexmont · Tavel · Lorimo · Feravi · Drastelmor</div>
  <div class="contact contact-stack" style="left:8px;top:195px;font-size:7.5px;gap:2px">
    <span><b>E.</b> info@tyreferns.example</span>
    <span><b>P.</b> +1 345 555 0142</span>
    <span><b>W.</b> tyreferns.example</span>
    <span><b>A.</b> 41 Marlow Lane</span>
  </div>
</div>

<!-- 160 x 600 -->
<div class="size-label" style="left:599px;top:493px">160 x 600</div>
<div class="ad" style="left:600px;top:524px;width:64px;height:241px">
  <div class="ad-photo" style="height:180px" role="img" aria-label="Photo: car wheel in a workshop"></div>
  <div class="brand" style="left:3px;top:14px;font-size:7.5px;gap:2px"><span class="brand-dot" style="width:7px;height:7px;border-width:1px"></span>Tyre Ferns</div>
  <div class="headline" style="left:3px;top:62px;font-size:8.5px"><span class="accent">Free</span> Tyre</div>
  <div class="headline" style="left:3px;top:71px;font-size:8.5px">Installation</div>
  <div class="tagline" style="left:3px;top:92px;width:60px;font-size:5px">We sell tyres in bulk and individually.</div>
  <div class="price-label" style="left:3px;top:113px;font-size:5px;white-space:normal;width:60px;line-height:1.2">Our tyres are priced from</div>
  <div class="price" style="left:3px;top:127px;font-size:9px">KYD$55-$60</div>
  <div class="cta" style="left:3px;top:142px;width:56px;height:11px;font-size:5.5px">Order now</div>
  <div class="contact contact-stack" style="left:3px;top:190px;font-size:5px;gap:6px">
    <span><b>E.</b> info@tyreferns.example</span>
    <span><b>P.</b> +1 345 555 0142</span>
    <span><b>W.</b> tyreferns.example</span>
    <span><b>A.</b> 41 Marlow Lane</span>
  </div>
</div>

<!-- 300 x 250 -->
<div class="size-label" style="left:452px;top:798px">300 x 250</div>
<div class="ad" style="left:452px;top:824px;width:121px;height:100px">
  <div class="ad-photo" style="height:86px" role="img" aria-label="Photo: car wheel in a workshop"></div>
  <div class="brand" style="left:5px;top:9px;font-size:8.5px;gap:3px"><span class="brand-dot" style="width:8px;height:8px;border-width:1px"></span>Tyre Ferns</div>
  <div class="headline" style="left:5px;top:32px;font-size:9.5px"><span class="accent">Free</span> Tyre</div>
  <div class="headline" style="left:5px;top:41px;font-size:9.5px">Installation</div>
  <div class="rule" style="left:5px;top:54px;width:20px;height:1px"></div>
  <div class="price-label" style="left:5px;top:59px;font-size:5.5px">Our tyres are priced from</div>
  <div class="price" style="left:5px;top:67px;font-size:12px">KYD$55-$60</div>
  <div class="contact contact-line" style="left:0;right:0;top:89px;font-size:6px"><b>P.</b> +1 345 555 0142 | <b>W.</b> tyreferns.example</div>
</div>

<!-- 250 x 250 -->
<div class="size-label" style="left:599px;top:798px">250 x 250</div>
<div class="ad" style="left:600px;top:824px;width:100px;height:100px">
  <div class="ad-photo" style="height:86px" role="img" aria-label="Photo: car wheel in a workshop"></div>
  <div class="brand" style="left:7px;top:7px;font-size:7.5px;gap:3px"><span class="brand-dot" style="width:7px;height:7px;border-width:1px"></span>Tyre Ferns</div>
  <div class="headline" style="left:7px;top:30px;font-size:9px"><span class="accent">Free</span> Tyre</div>
  <div class="headline" style="left:7px;top:39px;font-size:9px">Installation</div>
  <div class="price-label" style="left:7px;top:57px;font-size:5px;letter-spacing:.04em">Our tyres are priced from</div>
  <div class="price" style="left:7px;top:65px;font-size:12px">KYD$55-$60</div>
  <div class="contact contact-line" style="left:0;right:0;top:90px;font-size:4.6px"><b>P.</b> +1 345 555 0142 | <b>W.</b> tyreferns.example</div>
</div>

<!-- 728 x 90 -->
<div class="size-label" style="left:17px;top:962px">728 x 90</div>
<div class="ad" style="left:18px;top:987px;width:292px;height:36px">
  <div class="ad-photo" style="width:221px;height:36px" role="img" aria-label="Photo: mechanic and car wheel in a workshop"></div>
  <div class="brand" style="left:5px;top:13px;font-size:8px;gap:2px"><span class="brand-dot" style="width:7px;height:7px;border-width:1px"></span>Tyre Ferns</div>
  <div class="headline" style="left:60px;top:9px;font-size:9px"><span class="accent">Free</span> Tyre</div>
  <div class="headline" style="left:60px;top:18px;font-size:9px">Installation</div>
  <div class="rule" style="left:120px;top:7px;width:1px;height:22px"></div>
  <div class="price-label" style="left:126px;top:9px;font-size:5.5px;letter-spacing:.02em">Our tyres are priced from</div>
  <div class="price" style="left:126px;top:17px;font-size:12px">KYD$55-$60</div>
  <div class="contact contact-stack" style="left:226px;top:4px;font-size:5.5px;gap:3px">
    <span><b>E.</b> info@tyreferns.example</span>
    <span><b>P.</b> +1 345 555 0142</span>
    <span><b>W.</b> tyreferns.example</span>
  </div>
</div>

</body>
</html>
```